KVORB Student Exchange needs a brochure design

I need a brochure design for KVORB Student Exchange based in Auckland, New Zealand. I am responsible for outbound exchanges where I recruit local students from around New Zealand between the ages of 15 and 18 who are interested in going on an exchange overseas. Students can select from 12 different countries including America, France, Italy, the Netherlands, Spain, Ireland, Germany, Brazil Japan, and Argentina and choose the programme length from 3 months to an academic year (although we offer shorter programmes for some countries). I would like to attract students who are keen to learn about other cultures and experience something completely different to home. I would like to see vibrant colours and images that coveys fun, youthfulness and adventure.
Updates

Hi,

I have added pics and content for your viewing. 

Thanks.

Tessa

Hi,

Could I request that the designs are done on a tri-fold brochure

Also, I would like to see vibrant colours. So far, I have seen colours matching the logo (which is ok)  but I want to try and move away from that and start something fresh. Please look at the booklet and fee sheet which I have uploaded for ideas. 

I am wondering whether there is too much writing to fit on a tri fold brochure...
If you are having problems fitting everything in, please let me know.

I think the testimonial section could use up 2 spaces on the brochure. 

Target Market(s)

I would like to target teenagers who are interested in other cultures and want to enhance their language learning

Industry/Entity Type

Learn

Font styles to use
Serif
Sans Serif
Decorative

```html
<!DOCTYPE html>
<html lang="en">
<head>
<meta charset="utf-8">
<title>KVORB Student Exchange – Tri-fold Brochure</title>
<link href="https://fonts.googleapis.com/css2?family=Oswald:wght@500;700&family=Arimo:ital,wght@0,400;0,700;1,400&family=Caveat:wght@500&display=swap" rel="stylesheet">
<style>
:root{
  --bg:#6d6d6d;
  --navy:#1b2f7a;
  --blue:#1f56b3;
  --yellow:#ffe000;
  --aqua:#86d6dd;
  --teal:#34b3c4;
  --orange:#f28a1a;
  --red:#e8371d;
  --green:#8fd13b;
  --sky:#19a7e0;
  --rust:#f26b1d;
  --tan:#e7c9a2;
  --purple:#a44cc4;
  --grey:#9a9a9a;
  --note:#fff27a;
  --white:#ffffff;
  --ink:#1d1d1d;
}
*{box-sizing:border-box;margin:0;padding:0}
html,body{width:1200px;height:961px;overflow:hidden}
body{background:var(--bg);font-family:"Arimo",Arial,sans-serif;color:var(--ink);position:relative}
.spread{position:absolute;left:250px;width:700px;height:450px;display:flex;box-shadow:0 4px 14px rgba(0,0,0,.35)}
.spread--outside{top:24px}
.spread--inside{top:487px}
.panel{position:relative;width:233.33px;height:100%;overflow:hidden}
.photo{position:absolute}
.head{font-family:"Oswald",Impact,sans-serif;font-weight:700;text-transform:uppercase;letter-spacing:.2px}

/* page 1 */
.p1 .photo{left:0;top:0;width:100%;height:315px;background:linear-gradient(180deg,#c9b49a 0%,#8c7a6a 45%,#2c3550 100%)}
.p1 .vertical{position:absolute;left:4px;top:300px;transform:rotate(-90deg);transform-origin:left top;color:var(--white);font-size:27px;white-space:nowrap}
.p1 .pitch{position:absolute;left:46px;top:170px;width:182px;color:var(--white);font-size:10.3px;line-height:13.2px}
.p1 .side{position:absolute;left:0;top:315px;width:100%;height:135px;background:var(--yellow)}
.p1 .side h3{color:var(--navy);font-size:15px;padding:8px 0 0 24px}
.p1 .side .photo{left:0;top:34px;width:70px;height:101px;background:linear-gradient(160deg,#e8b98b,#c47a44 60%,#7a4b2a)}
.p1 .side p{position:absolute;left:78px;top:34px;width:150px;font-size:8.2px;line-height:10px;color:var(--navy)}
.p1 .side p+p{top:78px}

/* page 2 back cover */
.p2 .top{position:absolute;left:0;top:0;width:100%;height:300px;background:linear-gradient(180deg,#9fe0e4,var(--aqua))}
.p2 h2{color:var(--blue);font-size:20px;text-align:center;padding-top:12px}
.p2 .sub{text-align:center;font-size:7px;color:var(--ink)}
.steps{position:absolute;left:8px;top:54px;width:218px}
.step{display:flex;align-items:flex-start;gap:6px;margin-bottom:6px}
.step b{flex:0 0 72px;font-size:5px;line-height:6px;color:var(--white);padding:2px 3px;white-space:nowrap;overflow:hidden}
.step span{font-size:5.8px;line-height:7.2px}
.c-green{background:var(--green)}.c-sky{background:var(--sky)}.c-red{background:var(--red)}.c-tan{background:var(--tan)}.c-purple{background:var(--purple)}.c-grey{background:var(--grey)}.c-rust{background:var(--rust)}
.p2 .bottom{position:absolute;left:0;top:300px;width:100%;height:150px;background:var(--white)}
.p2 .more{font-size:6.4px;font-style:italic;text-align:center;padding-top:5px}
.logo{display:flex;align-items:center;gap:5px;color:var(--navy);font-family:"Oswald",Impact,sans-serif;font-weight:700;white-space:nowrap}
.logo i{display:block;border-radius:50%;background:var(--navy)}
.p2 .logo{margin:6px 0 0 14px;font-size:13px}
.p2 .logo i{width:16px;height:16px}
.contacts{list-style:none;margin:7px 0 0 14px;font-size:6.5px;line-height:8px}
.contacts li{display:flex;align-items:flex-start;gap:5px;margin-bottom:4px}
.contacts svg{flex:0 0 9px;width:9px;height:9px}
.contacts .label{font-size:5.5px;color:#555}

/* page 3 front cover */
.p3{background:var(--white)}
.p3 .photo{left:0;top:0;width:100%;height:245px;background:linear-gradient(180deg,#8ec6ee 0%,#b9d6ea 40%,#7d8a99 75%,#4d5a4c 100%)}
.p3 .band{position:absolute;top:245px;left:0;width:100%;height:42px;background:var(--yellow);color:var(--navy);font-size:22px;padding:4px 0 0 14px}
.p3 .slogan{position:absolute;top:287px;left:0;width:100%;height:80px;background:var(--navy);color:var(--white);font-family:"Oswald",Impact,sans-serif;font-weight:500;font-size:19px;line-height:22px;padding:12px 0 0 14px}
.p3 .logo{position:absolute;left:14px;top:382px;font-size:17px}
.p3 .logo i{width:22px;height:22px}
.p3 .tag{position:absolute;left:0;width:100%;top:420px;text-align:center;font-size:8.5px;color:var(--navy);font-weight:700}

/* page 4 programmes */
.p4{background:var(--white)}
.p4 .wash{position:absolute;left:0;top:0;width:100%;height:88px;background:linear-gradient(120deg,#ffe600 0%,#f4e44a 45%,#c6e33a 100%)}
.p4 h2{position:absolute;top:102px;left:14px;right:8px;color:var(--navy);font-size:14px;white-space:nowrap}
.p4 .lead{position:absolute;top:125px;left:14px;font-size:8px}
.prog{position:absolute;top:142px;left:8px;width:218px;font-size:6px;line-height:7.2px}
.prog .cols{display:flex;font-weight:700;font-size:5.5px;margin-bottom:3px}
.prog .cols span:first-child,.row span:first-child{flex:0 0 82px;padding-left:6px}
.prog .bar{font-weight:700;font-size:6.6px;padding:1px 6px;margin:3px 0 2px}
.prog .bar small{display:block;font-weight:400;font-size:5.3px;line-height:6px}
.row{display:flex}

/* page 5 testimonials */
.p5{background:var(--teal)}
.p5 h2{position:absolute;top:18px;left:0;width:100%;text-align:center;color:var(--white);font-size:14px}
.snap{position:absolute;border:3px solid var(--white);box-shadow:0 1px 3px rgba(0,0,0,.3)}
.s1{left:12px;top:44px;width:106px;height:78px;transform:rotate(-4deg);background:linear-gradient(150deg,#b7504a,#6e2d2d)}
.s2{left:120px;top:62px;width:100px;height:70px;transform:rotate(3deg);background:linear-gradient(150deg,#8d9db1,#3c4658)}
.s3{left:18px;top:130px;width:86px;height:66px;transform:rotate(3deg);background:linear-gradient(150deg,#d4b48a,#7b5b3b)}
.p5 .note{position:absolute;left:104px;top:150px;width:114px;height:112px;background:var(--note);transform:rotate(-6deg);font-family:"Caveat",cursive;font-size:9.5px;line-height:10.5px;color:#23306e;padding:10px 8px;box-shadow:1px 2px 4px rgba(0,0,0,.3)}
.p5 .quote{position:absolute;left:12px;top:278px;width:210px;color:var(--white);font-size:6.3px;line-height:8px}
.p5 .low{left:0;top:318px;width:100%;height:132px;background:linear-gradient(160deg,#6fb6e8,#4b7ea8 50%,#3a4d3a)}

/* page 6 testimonials */
.p6{background:var(--orange)}
.p6 .quote{position:absolute;color:var(--white);font-style:italic;font-size:6.6px;line-height:8.3px}
.p6 .q1{left:10px;top:14px;width:148px}
.p6 .q2{left:122px;top:150px;width:104px;font-style:normal}
.bubble{position:absolute;left:160px;top:40px;width:66px;height:48px}
.bubble span{position:absolute;inset:0;display:flex;align-items:center;justify-content:center;text-align:center;color:var(--white);font-family:"Oswald",Impact,sans-serif;font-weight:700;font-size:9.5px;line-height:10px;padding-bottom:6px}
.p6 .castle{left:6px;top:230px;width:116px;height:110px;background:linear-gradient(180deg,#8fc3e8,#c9a070 60%,#7a5a3a)}
.p6 .boys{left:92px;top:330px;width:141px;height:120px;background:linear-gradient(150deg,#7ab06a,#3d7a3d 55%,#2a3a2a)}
.p6 .kid{left:0;top:350px;width:90px;height:100px;background:linear-gradient(160deg,#e4c39a,#3f6a95)}
</style>
</head>
<body>

<section class="spread spread--outside" aria-label="Brochure outside">
  <div class="panel p1">
    <div class="photo" role="img" aria-label="Group of exchange students posing in a European city square"></div>
    <div class="vertical head">Student Exchange</div>
    <p class="pitch">Have the adventure of a lifetime<br>Immerse yourself in a new culture<br>Sharpen those language skills<br>Make awesome new friends<br>You'll gain confidence and a sense of independence that will probably exceed your expectations!</p>
    <div class="side">
      <h3 class="head">We are on your side</h3>
      <div class="photo" role="img" aria-label="Smiling student holding a souvenir"></div>
      <p>You are not just another client to us, not just another number. You choose the country and programme.</p>
      <p>We'll take care of the rest and as a non-profit organization, you can count on us to keep costs to a minimum.</p>
    </div>
  </div>

  <div class="panel p2">
    <div class="top">
      <h2 class="head">How to get started</h2>
      <p class="sub">After you have chosen your destination and programme</p>
      <div class="steps">
        <div class="step"><b class="c-green">Step 1. INITIAL APPLICATION</b><span>Complete the initial application form and post it to us with a $50 deposit (downloadable from our website).</span></div>
        <div class="step"><b class="c-sky">Step 2. FULL APPLICATION</b><span>We will get in touch with you and send you the full application form.</span></div>
        <div class="step"><b class="c-red">Step 3. INTERVIEW</b><span>Once you have submitted your full application form to us, we will arrange an interview with you and either both or one of your parents.</span></div>
        <div class="step"><b class="c-tan">Step 4. ACCEPTANCE</b><span>Once you are accepted, we will start arranging your flights, insurance, visa, host family and school placement.</span></div>
        <div class="step"><b class="c-purple">Step 5. ORIENTATION</b><span>You will have an orientation about a month prior to departure. This is to prepare you for your exchange. (You will also have an orientation in your host country.)</span></div>
        <div class="step"><b class="c-grey">Step 6. BON VOYAGE!</b><span>Now your adventure begins! A KVORB representative will be at the airport to send you off. Once you arrive on the other side, you will be met by the host organisation who will provide you with an orientation then help you transfer to your host family.</span></div>
      </div>
    </div>
    <div class="bottom">
      <p class="more">For more information on our exchange programmes, visit</p>
      <div class="logo"><i></i>KVORB Student Exchange</div>
      <ul class="contacts">
        <li><svg viewBox="0 0 10 10"><circle cx="5" cy="5" r="4.5" fill="#1f56b3"/><path d="M1 5h8M5 1c2 2 2 6 0 8M5 1c-2 2-2 6 0 8" stroke="#fff" stroke-width=".7" fill="none"/></svg><span><span class="label">Official Website:</span><br>www.kvorb-exchange.co.nz</span></li>
        <li><svg viewBox="0 0 10 10"><rect width="10" height="10" fill="#1f56b3"/></svg><span>social.example/kvorbexchange</span></li>
        <li><svg viewBox="0 0 10 10"><path d="M5 .5a3.3 3.3 0 0 1 3.3 3.3C8.3 6.2 5 9.5 5 9.5S1.7 6.2 1.7 3.8A3.3 3.3 0 0 1 5 .5z" fill="#e8371d"/><circle cx="5" cy="3.8" r="1.2" fill="#fff"/></svg><span>12 Harbour Lane/PO Box 40210<br>Parnell, Auckland, New Zealand 1052</span></li>
        <li><svg viewBox="0 0 10 10"><circle cx="5" cy="5" r="4.5" fill="#1f56b3"/><path d="M3.3 2.6l1 1.2-.6.8c.4.9 1 1.5 1.8 1.9l.8-.6 1.2 1-.7 1c-2.3-.4-4-2.2-4.3-4.5z" fill="#fff"/></svg><span>09 555 0142, 0800 555 019</span></li>
        <li><svg viewBox="0 0 10 10"><circle cx="5" cy="5" r="4.5" fill="#1f56b3"/><rect x="2.5" y="3.2" width="5" height="3.6" fill="#fff"/><path d="M2.5 3.2L5 5.3l2.5-2.1" stroke="#1f56b3" stroke-width=".6" fill="none"/></svg><span>tessa@kvorb.co.nz</span></li>
      </ul>
    </div>
  </div>

  <div class="panel p3">
    <div class="photo" role="img" aria-label="Two students in winter coats posing in front of a fairytale castle"></div>
    <div class="band head">Student Exchange</div>
    <div class="slogan">The time of your life;<br>An experience for life</div>
    <div class="logo"><i></i>KVORB Student Exchange</div>
    <p class="tag">non-profit, charitable organisation</p>
  </div>
</section>

<section class="spread spread--inside" aria-label="Brochure inside">
  <div class="panel p4">
    <div class="wash" role="img" aria-label="Bright yellow-green wash with a faded student photo"></div>
    <h2 class="head">Programmes to choose from</h2>
    <p class="lead">Select your programme and destination:</p>
    <div class="prog">
      <div class="cols"><span>DEPARTURE MONTH</span><span>DESTINATION OPTIONS</span></div>
      <div class="bar c-green">Six Week Programmes</div>
      <div class="row"><span>December</span><span>France, Italy</span></div>
      <div class="bar c-sky">Three Month Programmes<small>(other variations maybe possible)</small></div>
      <div class="row"><span>January</span><span>France, Germany, Ireland, Italy</span></div>
      <div class="row"><span>February</span><span>Spain only</span></div>
      <div class="row"><span>March</span><span>Argentina, Japan</span></div>
      <div class="row"><span>August</span><span>Argentina, Ireland</span></div>
      <div class="row"><span>September</span><span>France, Germany, Italy, Spain</span></div>
      <div class="bar c-rust">Semester Programmes<small>(a semester is of 4, 5 or 6 months duration)</small></div>
      <div class="row"><span>January</span><span>Brazil, France, Germany,<br>Ireland, Italy, Netherlands, USA</span></div>
      <div class="row"><span>February</span><span>Argentina, Spain</span></div>
      <div class="row"><span>March</span><span>Japan only</span></div>
      <div class="row"><span>July</span><span>Brazil only</span></div>
      <div class="row"><span>August</span><span>Argentina, Belgium, France,<br>Germany, Ireland, Japan,<br>Netherlands, USA</span></div>
      <div class="row"><span>September</span><span>France, Germany, Italy, Spain</span></div>
      <div class="bar c-tan">School Year Programme<small>(a school year is of 10 or 11 months duration)</small></div>
      <div class="row"><span>January</span><span>Brazil, France, Germany, Italy,<br>Netherlands</span></div>
      <div class="row"><span>February</span><span>Argentina, Spain</span></div>
      <div class="row"><span>March</span><span>Japan only</span></div>
      <div class="row"><span>July</span><span>Brazil only</span></div>
      <div class="row"><span>August</span><span>Argentina, Belgium, France,<br>Germany, Ireland, Netherlands, USA</span></div>
      <div class="row"><span>September</span><span>France, Germany, Italy, Japan, Spain</span></div>
    </div>
  </div>

  <div class="panel p5">
    <h2 class="head">What students have said</h2>
    <div class="snap s1" role="img" aria-label="Host family gathered around a dinner table"></div>
    <div class="snap s2" role="img" aria-label="Exchange students together at a winter event"></div>
    <div class="snap s3" role="img" aria-label="Student with new friends at school"></div>
    <div class="note">My host family made me feel at home from day one. I tried new food, learnt the language fast and made friends I will keep forever. Best year of my life! – Aroha, Tarrowvale College, Academic Year in Germany</div>
    <p class="quote">"I was so lucky with my host family placement. They were such good people, really funny and kind and were always taking me travelling and showing me new places. I couldn't have asked for a better placement." Jordan, Quellin Park College, Academic Year in Italy</p>
    <div class="photo low" role="img" aria-label="Smiling student on a city street with historic buildings"></div>
  </div>

  <div class="panel p6">
    <p class="quote q1">"I was lucky to get lots of trips with my host family and also with new friends from school. I loved the food, the festivals and the people. I improved my language so much and came home more confident and independent. I would recommend an exchange to anyone thinking about it!" Mia, Merrowdene Girls' College, Academic Year in Japan</p>
    <div class="bubble">
      <svg viewBox="0 0 66 48" width="66" height="48" aria-hidden="true"><ellipse cx="33" cy="21" rx="32" ry="20" fill="#e8371d" stroke="#fff" stroke-width="1.5"/><path d="M18 36l-6 11 16-8z" fill="#e8371d" stroke="#fff" stroke-width="1.5"/></svg>
      <span>WHAT<br>STUDENTS<br>HAVE SAID</span>
    </div>
    <p class="quote q2">"I would recommend doing an exchange for a year as this gives you a good understanding of the language and culture. I love my host family. I was so lucky that my host brother was about my age so we got on really well." Hannah, Fennick Heights High School, Academic Year in Spain</p>
    <div class="photo castle" role="img" aria-label="Historic cathedral under a blue sky"></div>
    <div class="photo kid" role="img" aria-label="Student giving a thumbs up outdoors"></div>
    <div class="photo boys" role="img" aria-label="Group of students in traditional festival jackets"></div>
  </div>
</section>

</body>
</html>
```